Brightpath Letterhead

We would like a letterhead for our company. I have uploaded our logo.

Brightpath Ridge Consulting
1450 W Corliss Ave Ste 310
Arlington, TX 76006
833-517-2906

```html
<!DOCTYPE html>
<html lang="en">
<head>
<meta charset="utf-8">
<title>Brightpath Ridge Consulting Letterhead</title>
<link href="https://fonts.googleapis.com/css2?family=Open+Sans:wght@400;600&family=Poppins:wght@500;600&display=swap" rel="stylesheet">
<style>
  :root {
    --teal: #175f6e;
    --green: #67c191;
    --ink: #4f4f4f;
    --ink-dark: #333333;
    --paper: #ffffff;
    --rule: #d6d6d6;
  }
  * { box-sizing: border-box; margin: 0; padding: 0; }
  html, body { width: 1040px; height: 1200px; overflow: hidden; background: var(--paper); }
  .letterhead {
    position: relative;
    width: 1040px;
    height: 1200px;
    background: var(--paper);
    font-family: "Open Sans", Arial, sans-serif;
    color: var(--ink);
  }
  .top-bar { position: absolute; top: 0; left: 0; right: 0; height: 16px; background: var(--green); }

  .brand {
    position: absolute; top: 44px; left: 110px;
    display: flex; align-items: center; gap: 14px;
  }
  .brand-dot { width: 40px; height: 40px; border-radius: 50%; background: var(--teal); }
  .brand-name {
    font-family: "Poppins", Arial, sans-serif;
    font-weight: 600; font-size: 23px; letter-spacing: 2.5px;
    text-transform: uppercase; color: var(--teal);
  }

  .contact-phone {
    position: absolute; top: 36px; left: 700px;
    height: 38px; padding-left: 18px;
    border-left: 1px solid var(--rule);
    display: flex; align-items: center; gap: 10px;
    font-family: "Poppins", Arial, sans-serif;
    font-weight: 600; font-size: 23px; letter-spacing: 0.5px; color: var(--teal);
  }
  .contact-phone svg { width: 32px; height: 32px; }

  .letter-body {
    position: absolute; top: 214px; left: 98px; width: 745px;
    font-size: 15px;
  }
  .issue-date { margin-bottom: 18px; }
  .recipient { line-height: 19px; margin-bottom: 52px; }
  .salutation { margin-bottom: 30px; }
  .letter-body p.para {
    line-height: 27.5px; text-align: justify; margin-bottom: 27px;
  }
  .closing { margin-top: 52px; }
  .signatory { margin-top: 56px; }
  .signatory-name { font-size: 19px; color: var(--ink-dark); font-weight: 400; }
  .signatory-title { font-size: 15px; margin-top: 6px; }

  .footer-band {
    position: absolute; left: 0; right: 0; bottom: 0; height: 76px;
    background: var(--teal); color: var(--paper);
    padding: 18px 0 0 110px;
    font-family: "Poppins", Arial, sans-serif; font-weight: 600;
    font-size: 18px; line-height: 22px;
  }
  .footer-band .company { text-transform: uppercase; }
</style>
</head>
<body>
  <main class="letterhead">
    <div class="top-bar"></div>

    <header>
      <div class="brand">
        <span class="brand-dot"></span>
        <span class="brand-name">Brightpath Ridge Consulting</span>
      </div>
      <div class="contact-phone">
        <svg viewBox="0 0 32 32" aria-hidden="true">
          <circle cx="16" cy="16" r="16" fill="var(--green)"/>
          <path d="M11.2 8.5c.6-.4 1.4-.3 1.8.3l1.8 2.6c.4.6.3 1.3-.2 1.8l-1.2 1.1c.9 1.9 2.3 3.4 4.2 4.4l1.2-1.1c.5-.5 1.3-.5 1.8-.1l2.5 1.9c.6.4.7 1.3.2 1.8l-1.3 1.5c-.8.9-2.1 1.2-3.2.7-4.5-1.9-7.8-5.3-9.6-9.9-.4-1.1 0-2.4.9-3.1z" fill="#ffffff"/>
        </svg>
        <span>833-517-2906</span>
      </div>
    </header>

    <section class="letter-body">
      <p class="issue-date">Issuing Date: May 5, 2018</p>
      <p class="recipient">Name Of Employee Mr. XYZABC<br>Address of Employee<br>Address Line 2 etc..</p>
      <p class="salutation">Dear Mr.XYZABC</p>
      <p class="para">Lorem Ipsum has been the industry's standard dummy text ever since the 1500s, when an unknown printer took a galley of type and scrambled it to make a type specimen book. It has survived not only five centuries, but also the leap into electronic typesetting, remaining essentially unchanged. It was popularised in the 1960s with the release of Lettrafix sheets containing Lorem Ipsum passages, and more recently with desktop publishing software like Foliant PageSetter including versions of Lorem Ipsum.</p>
      <p class="para">Lorem Ipsum is simply dummy text of the printing and typesetting industry. Lorem Ipsum has been the industry's standard dummy text ever since the 1500s, when an unknown printer took a galley of type and scrambled it to make a type specimen book.</p>
      <p class="para">It has survived not only five centuries, but also the leap into electronic typesetting, remaining essentially unchanged. It was popularised in the 1960s with the release of Lettrafix sheets containing Lorem IpsumIpsum passages.</p>
      <p class="closing">Yours Sincerely</p>
      <div class="signatory">
        <p class="signatory-name">Marcus Ellery</p>
        <p class="signatory-title">Managing Director</p>
      </div>
    </section>

    <footer class="footer-band">
      <div class="company">Brightpath Ridge Consulting</div>
      <div class="address">1450 W Corliss Ave Ste 310, Arlington, TX 76006</div>
    </footer>
  </main>
</body>
</html>
```